Update our OBGYN business card look and info

We are an OBGYN office. Our logo is nice but would like to "woman" part of the logo to be a darker color, to contrast with the flower that surrounds it. Maybe make our practice name Harbor Bloom Care Clinic more feminine. Our practice caters to women only. All providers and staff are female.

Target Market(s)

Females 16-65.

Industry/Entity Type

Business

Contact Information for Business Card

See attached upload. The ONLY CHANGE to the information is DELETE the name Dorothy Kemplin, Midwife and REPLACE with Greta Poundsworth, Midwife

Logo Text

Harbor Bloom Care Clinic Obstetrics & Gynecology

Font styles to use
Serif
Script

Colors
85cae6
0692cd
33a6d7
85abd2
f59195
eea4c8
cadf82
fac994
d3a5cc

```html
<!DOCTYPE html>
<html lang="en">
<head>
<meta charset="utf-8">
<title>Harbor Bloom Care Clinic – Business Card</title>
<link rel="stylesheet" href="https://fonts.googleapis.com/css2?family=Cinzel:wght@500&family=Montserrat:wght@400;600;700&display=swap">
<style>
  :root {
    --stage: #1f1f21;
    --card-dark: #3a3a3c;
    --card-light: #f7f7f5;
    --teal: #74bcd0;
    --ink: #3b3b3d;
    --grey: #6c6c6e;
    --white: #ffffff;
  }
  * { box-sizing: border-box; margin: 0; padding: 0; }
  html, body { width: 1200px; height: 800px; overflow: hidden; }
  body {
    background: var(--stage);
    font-family: "Montserrat", sans-serif;
    position: relative;
  }
  .card {
    position: absolute;
    width: 630px;
    height: 360px;
    box-shadow: 0 14px 30px rgba(0,0,0,.45);
    overflow: hidden;
  }
  /* Front card */
  .card--front {
    left: 480px; top: 40px;
    background: var(--card-dark);
  }
  .front__brand {
    position: absolute;
    left: 150px; top: 120px;
    display: flex; align-items: center; gap: 18px;
  }
  .brand__dot {
    width: 54px; height: 54px; border-radius: 50%;
    background: var(--teal);
    flex: none;
  }
  .brand__name {
    font-family: "Cinzel", serif;
    font-weight: 500;
    color: var(--teal);
    font-size: 19px;
    letter-spacing: .5px;
    white-space: nowrap;
  }
  .brand__tagline {
    font-family: "Montserrat", sans-serif;
    font-weight: 600;
    font-size: 17px;
    margin-top: 4px;
    white-space: nowrap;
  }
  .card--front .brand__tagline { color: var(--white); }
  .front__web {
    position: absolute;
    left: 0; right: 0; top: 250px;
    text-align: center;
    color: var(--white);
    font-size: 14px;
    letter-spacing: 2px;
  }
  .front__web strong { color: var(--teal); font-weight: 600; }

  /* Back card */
  .card--back {
    left: 100px; top: 390px;
    background: var(--card-light);
  }
  .back__brand {
    position: absolute;
    left: 40px; top: 36px;
    display: flex; align-items: center; gap: 16px;
  }
  .card--back .brand__tagline { color: var(--grey); }
  .back__rule {
    position: absolute;
    left: 44px; top: 130px;
    width: 76px; height: 3px;
    background: var(--teal);
  }
  .providers {
    position: absolute;
    left: 44px; top: 160px;
    list-style: none;
    color: var(--ink);
    font-size: 15px;
    line-height: 21px;
    white-space: nowrap;
  }
  .providers b { font-weight: 700; }
  .contacts {
    position: absolute;
    left: 340px; top: 178px;
    list-style: none;
    color: var(--ink);
    font-size: 15px;
    line-height: 21px;
  }
  .contacts li { display: flex; align-items: center; gap: 10px; white-space: nowrap; }
  .contacts svg { width: 14px; height: 14px; flex: none; }
  .contacts b { font-weight: 700; }
  .back__band {
    position: absolute;
    left: 0; right: 0; bottom: 0;
    height: 50px;
    background: var(--card-dark);
    color: var(--white);
    font-size: 12px;
    line-height: 50px;
    padding-left: 30px;
    white-space: nowrap;
  }
  .back__band b { font-weight: 700; }
</style>
</head>
<body>

<section class="card card--front" aria-label="Card front">
  <div class="front__brand">
    <span class="brand__dot"></span>
    <div>
      <div class="brand__name">HARBOR BLOOM CARE CLINIC</div>
      <div class="brand__tagline">Obstetrics &amp; Gynecology</div>
    </div>
  </div>
  <p class="front__web">www.<strong>harborbloomcare</strong>.com</p>
</section>

<section class="card card--back" aria-label="Card back">
  <div class="back__brand">
    <span class="brand__dot"></span>
    <div>
      <div class="brand__name">HARBOR BLOOM CARE CLINIC</div>
      <div class="brand__tagline">Obstetrics &amp; Gynecology</div>
    </div>
  </div>
  <div class="back__rule"></div>

  <ul class="providers">
    <li><b>Marion Castell,</b> MD</li>
    <li><b>Nadine Prewitt,</b> MD</li>
    <li><b>Helen Varga,</b> MD</li>
    <li><b>Greta Poundsworth,</b> Midwife</li>
    <li><b>Lena Brightwater,</b> Midwife</li>
  </ul>

  <ul class="contacts">
    <li>
      <svg viewBox="0 0 16 16" aria-hidden="true"><path d="M4 1.5l2.3 3-1.4 1.6a9 9 0 0 0 5 5l1.6-1.4 3 2.3-1.3 2.4C8 14.6 1.4 8 1.6 2.8z" fill="none" stroke="#74bcd0" stroke-width="1.4"/></svg>
      <span>(555) 014-2270</span>
    </li>
    <li>
      <svg viewBox="0 0 16 16" aria-hidden="true"><rect x="4" y="1.5" width="8" height="4" fill="none" stroke="#74bcd0" stroke-width="1.4"/><rect x="1.5" y="5.5" width="13" height="6" rx="1" fill="#74bcd0"/><rect x="4" y="10" width="8" height="4.5" fill="#fff" stroke="#74bcd0" stroke-width="1.4"/></svg>
      <span>(555) 014-2291</span>
    </li>
    <li>
      <svg viewBox="0 0 16 16" aria-hidden="true"><rect x="1.5" y="3.5" width="13" height="9" fill="none" stroke="#74bcd0" stroke-width="1.4"/><path d="M1.5 3.5L8 9l6.5-5.5" fill="none" stroke="#74bcd0" stroke-width="1.4"/></svg>
      <span>info@harborbloomcare.com</span>
    </li>
    <li>
      <svg viewBox="0 0 16 16" aria-hidden="true"><circle cx="8" cy="8" r="6.3" fill="none" stroke="#74bcd0" stroke-width="1.4"/><ellipse cx="8" cy="8" rx="2.8" ry="6.3" fill="none" stroke="#74bcd0" stroke-width="1.2"/><path d="M1.7 8h12.6" stroke="#74bcd0" stroke-width="1.2"/></svg>
      <span>www.<b>harborbloomcare</b>.com</span>
    </li>
  </ul>

  <div class="back__band"><b>Harbor Bloom Care Clinic,</b> 418 Linden Avenue, Suite 3B, Dalton Ridge, GA 30999</div>
</section>

</body>
</html>
```